Gentle Harbor Coaching Brochure

I want a brochure that I can either send out to clients via email or that I can print and have sitting on counters or displays
a) either be placed on counters; or
b) be sent digitally to people
I want to help people understand what coaching is, how it can help them. I want them to understand what it is and also what it isn't.
I want a call to action at the end to get them to contact me and book a conversation.

Target Market(s)

My target market is primarily people over 40 who are stuck, frustrated, ready to change.

Industry/Entity Type

Business and Personal

Font styles to use
Sans Serif

Colors
0094D4
00A9DD
6FCCEA
C7EBF8
E9F6FB
EE7325
F08F49
F5BC92
FAE3D3
FDF4ED
6B429C
8869AF
B7A5CE
E3DAEB
F3F0F8

Requirements
Must have
• My project must have the option of either sending out a digital copy or be printed in hard copy and easy to fold so it doesn't take up too much space on a counter.
Nice to have
• Images would be welcome, my business card has curves in it, so it would be nice to have that theme carried on in the design of the brochure

```html
<!DOCTYPE html>
<html lang="en">
<head>
<meta charset="utf-8">
<title>Gentle Harbor Coaching – Trifold Brochure</title>
<link rel="stylesheet" href="https://fonts.googleapis.com/css2?family=Roboto+Condensed:ital,wght@0,300;0,400;0,700;1,400;1,700&family=Roboto:ital,wght@0,700;0,900;1,700;1,900&display=swap">
<style>
  :root {
    --orange: #f2912b;
    --orange-deep: #ee7325;
    --peach: #f3dcb5;
    --peach-soft: #fae3d3;
    --cream: #fdf4ed;
    --ink: #333333;
    --ink-soft: #4a4a4a;
    --link: #1f6fb8;
    --logo-tone: #8f8270;
    --white: #ffffff;
  }
  * { box-sizing: border-box; margin: 0; padding: 0; }
  html, body { width: 680px; height: 1200px; overflow: hidden; background: var(--white); }
  body { position: relative; font-family: "Roboto Condensed", Arial, sans-serif; color: var(--ink); }

  .spread { position: absolute; left: 59px; width: 562px; height: 436px; overflow: hidden; background: var(--white); }
  .spread--outside { top: 75px; }
  .spread--inside { top: 572px; }
  .spread__shapes { position: absolute; inset: 0; }

  .panel { position: absolute; top: 0; width: 187.3px; height: 436px; }
  .panel--1 { left: 0; }
  .panel--2 { left: 187.3px; }
  .panel--3 { left: 374.6px; }

  .abs { position: absolute; }
  .body-text { font-size: 8.6px; line-height: 11px; color: var(--ink); }
  .link { color: var(--link); font-family: "Roboto", Arial, sans-serif; font-weight: 700; font-style: italic; }

  /* outside: back panel */
  .intro-techniques { left: 16px; top: 30px; width: 166px; }
  .intro-permission { left: 16px; top: 86px; width: 170px; }
  .free-offer { left: 10px; top: 140px; width: 170px; text-align: center; font-size: 12.4px; line-height: 15.2px; font-weight: 700; color: var(--ink-soft); }
  .free-offer .accent { color: var(--orange); font-weight: 400; }
  .email-note { left: 18px; top: 237px; width: 160px; }
  .web-note { left: 18px; top: 287px; width: 160px; }
  .first-step { left: 16px; top: 364px; width: 166px; font-size: 9.4px; line-height: 12px; color: var(--white); font-weight: 300; }
  .follow-note { left: 24px; top: 395px; font-size: 7px; font-weight: 700; color: var(--ink); }
  .follow-url { left: 17px; top: 405px; font-size: 7.6px; font-weight: 700; color: var(--ink); }

  /* outside: contact panel */
  .cta-headline { left: 10px; top: 33px; width: 167px; text-align: center; font-family: "Roboto", Arial, sans-serif; font-weight: 900; font-style: italic; color: var(--orange); font-size: 17px; line-height: 21.2px; }
  .cta-book { left: 0; top: 160px; width: 187px; text-align: center; font-family: "Roboto", Arial, sans-serif; font-weight: 700; font-style: italic; font-size: 11.6px; color: var(--ink); }
  .cta-phone-icon { left: 83px; top: 196px; }
  .cta-phone { left: 0; top: 214px; width: 187px; text-align: center; font-family: "Roboto", Arial, sans-serif; font-weight: 900; font-style: italic; font-size: 17px; color: var(--ink); }
  .cta-at { left: 0; top: 232px; width: 187px; text-align: center; font-family: "Roboto", Arial, sans-serif; font-weight: 700; font-size: 19px; color: var(--orange); }
  .cta-email { left: 0; top: 255px; width: 187px; text-align: center; font-family: "Roboto", Arial, sans-serif; font-weight: 700; font-style: italic; font-size: 8.6px; color: var(--ink); }
  .brand-seal { left: 75px; top: 357px; width: 38px; height: 38px; border-radius: 50%; background: var(--white); display: flex; align-items: center; justify-content: center; text-align: center; font-size: 6.4px; line-height: 7px; color: var(--orange); font-weight: 700; }
  .cta-web { left: 0; top: 402px; width: 187px; text-align: center; font-family: "Roboto", Arial, sans-serif; font-weight: 700; font-style: italic; font-size: 9.6px; color: var(--white); }

  /* outside: cover */
  .brand-name { left: 0; top: 62px; width: 187px; text-align: center; font-size: 15px; font-weight: 300; letter-spacing: 1px; color: var(--logo-tone); }
  .cover-photo { left: 14px; top: 122px; width: 166px; height: 232px; border-radius: 60px 60px 0 0; background: radial-gradient(ellipse at 50% 30%, #c89a86 0 18%, #7b5440 19% 30%, transparent 31%), linear-gradient(180deg, #e6e3e0 0%, #8a8f96 55%, #6e747c 100%); }
  .cover-tagline { left: 12px; top: 372px; width: 170px; text-align: center; font-size: 11px; line-height: 14px; font-weight: 300; color: var(--cream); }
  .cover-name { left: 0; top: 406px; width: 187px; text-align: center; font-family: "Roboto", Arial, sans-serif; font-weight: 900; font-size: 12px; letter-spacing: 0.4px; color: var(--white); }

  /* inside: welcome */
  .portrait { left: 23px; top: 25px; width: 80px; height: 87px; background: linear-gradient(180deg, #8a6548 0%, #b98a62 55%, #c79a6e 100%); }
  .coach-name { left: 113px; top: 77px; font-family: "Roboto Condensed", Arial, sans-serif; font-style: italic; font-weight: 700; font-size: 9.4px; color: var(--orange); }
  .coach-role { left: 114px; top: 90px; font-style: italic; font-weight: 700; font-size: 6.4px; color: var(--ink); }
  .welcome-head { left: 23px; top: 128px; width: 165px; font-family: "Roboto", Arial, sans-serif; font-weight: 700; font-style: italic; font-size: 12.2px; line-height: 15.3px; color: var(--orange); }
  .welcome-body { left: 22px; top: 185px; width: 160px; font-size: 9.6px; line-height: 11.8px; color: var(--ink); }
  .curve-field { left: 10px; top: 275px; width: 240px; height: 161px; background: radial-gradient(ellipse at 40% 70%, rgba(243,220,181,0.55), rgba(255,255,255,0) 70%); }

  /* inside: benefits */
  .team-photo { left: 18px; top: 24px; width: 148px; height: 81px; background: linear-gradient(135deg, #d9d2c8 0%, #9c8a78 45%, #e9e4dd 100%); }
  .section-head { font-family: "Roboto Condensed", Arial, sans-serif; font-weight: 700; color: var(--orange); }
  .benefits-head { left: 15px; top: 128px; width: 165px; font-size: 12.4px; line-height: 15.4px; }
  .benefits-body { left: 15px; top: 168px; width: 165px; }
  .why-head { left: 15px; top: 268px; font-family: "Roboto", Arial, sans-serif; font-weight: 900; font-size: 12.6px; color: var(--orange); }
  .why-list { left: 15px; top: 290px; width: 157px; list-style: none; }
  .why-list li { height: 19.2px; margin-bottom: 0.8px; background: var(--orange); display: flex; align-items: center; gap: 6px; padding-left: 4px; font-family: "Roboto", Arial, sans-serif; font-weight: 900; font-style: italic; font-size: 8.9px; color: var(--white); }
  .why-list svg { width: 12px; height: 12px; flex: none; }

  /* inside: approach */
  .office-photo { left: 0; top: 0; width: 187.3px; height: 212px; background: linear-gradient(180deg, #f4eee6 0%, #e4d2bb 50%, #f0e6d9 100%); }
  .session-photo { left: 17px; top: 149px; width: 148px; height: 81px; background: linear-gradient(90deg, #d9d4cf 0%, #c8a48e 35%, #2e4256 70%, #cfd6dc 100%); }
  .approach-head { left: 18px; top: 244px; width: 165px; font-size: 12.4px; line-height: 15.4px; }
  .approach-body { left: 18px; top: 288px; width: 160px; }
  .approach-body-2 { left: 18px; top: 343px; width: 160px; }
</style>
</head>
<body>

<section class="spread spread--outside" aria-label="Brochure outside">
  <svg class="spread__shapes" viewBox="0 0 562 436" width="562" height="436" aria-hidden="true">
    <defs>
      <linearGradient id="foldShade" x1="0" x2="1">
        <stop offset="0" stop-color="#d8d8d8"/><stop offset="0.25" stop-color="#ffffff"/>
      </linearGradient>
      <linearGradient id="curveGlow" x1="0" x2="1">
        <stop offset="0" stop-color="#f3dcb5" stop-opacity="0"/><stop offset="0.5" stop-color="#f3dcb5" stop-opacity="0.55"/><stop offset="1" stop-color="#f3dcb5" stop-opacity="0"/>
      </linearGradient>
    </defs>
    <rect x="0" y="0" width="187.3" height="436" fill="var(--peach)"/>
    <rect x="374.6" y="0" width="187.4" height="436" fill="url(#foldShade)"/>
    <path d="M187.3,280 C240,300 300,380 380,320 C440,280 500,300 562,270 L562,330 C500,350 440,330 380,365 C300,410 240,330 187.3,330 Z" fill="url(#curveGlow)" role="img" aria-label="Soft flowing line pattern"/>
  </svg>

  <div class="panel panel--1">
    <p class="abs body-text intro-techniques">Our coaching is based on neuroscience, and in some cases, we also use neuro-linguistic programming, hypnosis, timeline therapy, meditation, and mindset exercises.</p>
    <p class="abs body-text intro-permission">We always ask for your permission before introducing any of these techniques, and you'll never do anything you don't want to do.</p>
    <p class="abs free-offer">If you're interested in finding out more, we offer a <span class="accent">FREE</span> 30-45 minute conversation to see if coaching is right for you.</p>
    <p class="abs body-text email-note">Simply email us at :<br><span class="link">info@gentleharbor.com.au</span> with your contact number, and we'll call you back within 48 hours to schedule a time.</p>
    <p class="abs body-text web-note">You can also visit our website at<br><span class="link">www.gentleharbor.com.au</span><br>for more information.</p>
  </div>

  <svg class="spread__shapes" viewBox="0 0 562 436" width="562" height="436" aria-hidden="true">
    <path d="M0,358 C60,340 130,328 187.3,326 C250,326 300,352 370,350 C440,348 500,320 562,308 L562,436 L0,436 Z" fill="var(--orange)"/>
  </svg>

  <div class="panel panel--1">
    <p class="abs first-step">Visit Gentle Harbor and take the first step towards a brighter future.</p>
    <p class="abs follow-note">Please support us by following our news page</p>
    <p class="abs follow-url">https://www.gentleharbor.com.au/news</p>
  </div>

  <div class="panel panel--2">
    <h1 class="abs cta-headline">Join Me as I Help You Reshape your Future into One that Inspires You</h1>
    <p class="abs cta-book">BOOK A FREE Chat</p>
    <svg class="abs cta-phone-icon" width="20" height="20" viewBox="0 0 20 20" aria-hidden="true">
      <circle cx="10" cy="10" r="8.8" fill="none" stroke="var(--orange)" stroke-width="1.6"/>
      <path d="M7,5.5 L8.6,7.6 L7.6,8.8 C8.3,10.4 9.6,11.7 11.2,12.4 L12.4,11.4 L14.5,13 L13.3,14.5 C9.5,14.2 5.8,10.5 5.5,6.7 Z" fill="var(--orange)"/>
    </svg>
    <p class="abs cta-phone">0400 555 018</p>
    <p class="abs cta-at">@</p>
    <p class="abs cta-email">info@gentleharbor.com.au</p>
    <div class="abs brand-seal">Gentle<br>Harbor</div>
    <p class="abs cta-web">www.gentleharbor.com.au</p>
  </div>

  <div class="panel panel--3">
    <p class="abs brand-name">GENTLE HARBOR</p>
    <div class="abs cover-photo" role="img" aria-label="Portrait photo of the coach in a grey blazer, arms crossed"></div>
  </div>

  <svg class="spread__shapes" viewBox="0 0 562 436" width="562" height="436" aria-hidden="true">
    <path d="M374.6,350 C440,348 500,320 562,308 L562,436 L374.6,436 Z" fill="var(--orange)"/>
  </svg>

  <div class="panel panel--3">
    <p class="abs cover-tagline">Bring balance back into your business, health &amp; life Your Coach &amp; Consultant,</p>
    <p class="abs cover-name">MAREN ELLIS</p>
  </div>
</section>

<section class="spread spread--inside" aria-label="Brochure inside">
  <svg class="spread__shapes" viewBox="0 0 562 436" width="562" height="436" aria-hidden="true">
    <defs>
      <linearGradient id="foldShadeIn" x1="0" x2="1">
        <stop offset="0.75" stop-color="#ffffff"/><stop offset="1" stop-color="#dcdcdc"/>
      </linearGradient>
    </defs>
    <rect x="0" y="0" width="187.3" height="436" fill="url(#foldShadeIn)"/>
    <rect x="187.3" y="0" width="187.3" height="436" fill="url(#foldShadeIn)"/>
    <rect x="0" y="0" width="374.6" height="60" fill="var(--orange)"/>
  </svg>

  <div class="panel panel--1">
    <div class="abs curve-field" role="img" aria-label="Soft flowing line pattern"></div>
    <div class="abs portrait" role="img" aria-label="Photo of the coach smiling, seated"></div>
    <p class="abs coach-name">MAREN ELLIS</p>
    <p class="abs coach-role">Coach &amp; Consultant</p>
    <h2 class="abs welcome-head">Welcome to Gentle Harbor coaching, where we help you achieve your full potential.</h2>
    <p class="abs welcome-body">We offer a safe and supportive environment to help you change unhelpful habits, gain insights into creating the outcomes you want, and harness your strengths to overcome any challenge you may face.</p>
  </div>

  <div class="panel panel--2">
    <div class="abs team-photo" role="img" aria-label="Photo of colleagues meeting around a table with a laptop"></div>
    <h2 class="abs section-head benefits-head">Wondering what coaching can do for you?</h2>
    <p class="abs body-text benefits-body">It can help you get that next promotion, ramp up your leadership or management style, deal with a particular situation or decision, change your career, or find that dream job. But coaching isn't just for work - it can also help you create healthier habits, relationships, and achieve any number of life goals.</p>
    <h2 class="abs why-head">Why Choose Me?</h2>
    <ul class="abs why-list">
      <li><svg viewBox="0 0 12 12" aria-hidden="true"><circle cx="6" cy="6" r="5" fill="none" stroke="#fff" stroke-width="1"/><path d="M3.5,6.2 L5.3,8 L8.6,4.3" fill="none" stroke="#fff" stroke-width="1.1"/></svg>Results Driven</li>
      <li><svg viewBox="0 0 12 12" aria-hidden="true"><path d="M1.5,2 H10.5 V8 H5 L2.5,10.2 V8 H1.5 Z" fill="none" stroke="#fff" stroke-width="1"/></svg>Free Consultations</li>
      <li><svg viewBox="0 0 12 12" aria-hidden="true"><circle cx="4" cy="4" r="1.8" fill="none" stroke="#fff" stroke-width="1"/><circle cx="8.5" cy="4" r="1.8" fill="none" stroke="#fff" stroke-width="1"/><path d="M1,10.5 C1,7.5 7,7.5 7,10.5 M6,8 C7,7 11,7 11,10.5" fill="none" stroke="#fff" stroke-width="1"/></svg>Science meets art</li>
      <li><svg viewBox="0 0 12 12" aria-hidden="true"><path d="M6,10.5 C2,7.5 1,5.8 1,4.2 C1,2.6 2.3,1.5 3.6,1.5 C4.6,1.5 5.5,2.1 6,3 C6.5,2.1 7.4,1.5 8.4,1.5 C9.7,1.5 11,2.6 11,4.2 C11,5.8 10,7.5 6,10.5 Z" fill="none" stroke="#fff" stroke-width="1"/></svg>Personalised Approach</li>
    </ul>
  </div>

  <div class="panel panel--3">
    <div class="abs office-photo" role="img" aria-label="Softly blurred photo of a bright office interior"></div>
    <div class="abs session-photo" role="img" aria-label="Photo of a coach talking with a client across a table"></div>
    <h2 class="abs section-head approach-head">At Gentle Harbor, our coaching is self-directed,</h2>
    <p class="abs body-text approach-body">which means we help you find your own solutions. We focus on stretching you in the right ways to motivate your growth and guide you towards your goals.</p>
    <p class="abs body-text approach-body-2">Throughout the process, we maintain a positive attitude, encouraging and acknowledging your achievements every step of the way.</p>
  </div>
</section>

</body>
</html>
```